Guild of Lucid Observant Wanderers (GLOW!)

GLOW! is a 21st Century-proof Human Rights Movement working for the protection of democratic values and individual rights & towards the rebalancing of the global narrative on the issues that are driving public discourse and affairs.

Using our strength in numbers, GLOW! shall work towards the protection of our human rights in a manner that adequately reflects the challenges and opportunities of a hyper-digitized world.

The centerpiece of our movement is the introduction of the Pledge of Lanternfall. It allows global citizens, for the first time in the history of mankind, to boldly proclaim their sovereignty in relation to their governments and international bodies.

Inspired by the Harrowgate Accord, we are looking for a design that reflects the historic nature of the manifesto, and it should invite the signatories to want to proudly display the document.

(NB: The manifesto may not be reproduced or shared without the explicit consent of the author Maarten Kolbeck)

Target Market(s)

It targets the socially involved population

Industry/Entity Type

community & non-profit

Font styles to use
Decorative

Colors
EB3D1F
EC4F4E
F09395
F8D3D4
FCEDEE

Requirements
Must have
• Design that reflects the historic nature of the manifesto, and it should invite the signatories to want to proudly display the document.flect the
Nice to have
• A link with the Harrowgate Accord

```html
<!DOCTYPE html>
<html lang="en">
<head>
<meta charset="utf-8">
<title>Pledge of Lanternfall</title>
<link href="https://fonts.googleapis.com/css2?family=UnifrakturMaguntia&family=Arimo:wght@400;700&display=swap" rel="stylesheet">
<style>
  :root{
    --red:#eb3d1f;
    --coral:#ec4f4e;
    --rose:#f09395;
    --blush:#f8d3d4;
    --shell:#fcedee;
    --ink:#8f1d14;
    --stage:#e6e6e6;
  }
  html,body{margin:0;padding:0;width:891px;height:1200px;overflow:hidden;background:var(--stage);}
  .poster{
    position:absolute;left:40px;top:20px;width:811px;height:1160px;
    background:linear-gradient(180deg,#fffaf9 0%,var(--shell) 60%,var(--blush) 100%);
    box-shadow:0 2px 10px rgba(0,0,0,.12);
    overflow:hidden;
    font-family:"Arimo",Arial,sans-serif;
  }
  .frame{position:absolute;inset:18px;border:2px solid var(--red);}
  .frame-inner{position:absolute;inset:24px;border:1px solid var(--rose);}
  .quill-area{
    position:absolute;right:46px;top:30px;width:200px;height:34px;
    background:linear-gradient(90deg,rgba(248,211,212,.2),rgba(240,147,149,.45));
  }
  .title-band{
    position:absolute;left:46px;right:46px;top:70px;height:66px;
    display:flex;align-items:center;
    border-top:3px solid var(--red);border-bottom:3px solid var(--red);
  }
  .title-band::after{content:"";position:absolute;left:0;right:0;bottom:5px;border-bottom:1px solid var(--coral);}
  .title{
    margin:0 0 0 28px;font-family:"UnifrakturMaguntia",serif;font-weight:400;
    font-size:46px;color:var(--red);letter-spacing:1px;
  }
  .capitol{
    position:absolute;right:34px;bottom:150px;width:300px;height:330px;
    background:radial-gradient(ellipse at 50% 70%,rgba(255,255,255,.7),rgba(248,211,212,.25) 70%,transparent);
    border-radius:50% 50% 4px 4px/40% 40% 4px 4px;
  }
  .flag{
    position:absolute;left:0;right:0;bottom:0;height:190px;
    background:linear-gradient(170deg,rgba(240,147,149,.12) 0%,rgba(235,61,31,.22) 45%,rgba(143,40,60,.32) 100%);
  }
  .articles{
    position:absolute;left:56px;right:56px;top:156px;
    margin:0;padding:0;list-style:none;
    font-size:13.4px;line-height:20px;color:var(--ink);
  }
  .articles li{position:relative;padding-left:16px;margin-bottom:11px;}
  .articles li::before{content:"";position:absolute;left:0;top:7px;width:6px;height:6px;border:1px solid var(--red);border-radius:50%;}
  .key{color:var(--red);font-weight:700;}
  .key-big{color:var(--red);font-weight:700;font-size:15.5px;}
  .mark{background:var(--blush);color:var(--red);}
</style>
</head>
<body>
<main class="poster">
  <div class="flag" role="img" aria-label="Softly faded waving flag across the bottom"></div>
  <div class="capitol" role="img" aria-label="Faint domed assembly hall illustration"></div>
  <div class="frame"></div>
  <div class="frame-inner"></div>
  <div class="quill-area" role="img" aria-label="Feather quill pen"></div>

  <header class="title-band">
    <h1 class="title">Pledge of Lanternfall</h1>
  </header>

  <ul class="articles">
    <li>The Pledge of Lanternfall, like the Harrowgate Accord before it, is a plain statement that the lives of free people are not gifts granted by any ruler, nor by the institutions that claim to speak for them. It is the duty of the citizen to defend this truth, and to restore the balance between the governed and those who govern.</li>
    <li>So, we hold these truths to be self-evident:</li>
    <li>That all Human Beings born into this world are part of The Human Race, and that everyone is created with Equal Rights under the Natural Law of our Existence; any social construct that departs from this fundamental truth is, in principle, to be rejected and shall be recognised as such.</li>
    <li>That we are Nations of Laws, and the People as a matter of principle, should at all times be granted the just Protection of, and access to, our Human Rights and Laws, ESPECIALLY as they pertain to <span class="key-big">FREEDOM OF SPEECH, PRIVACY AND BODILY INTEGRITY.</span></li>
    <li>That the necessity to protect and regulate the conscience of its leaders is reflected in the charters that shape the modern world, being the <span class="key">Council for Learning and Culture</span> statutes, the Common Charter of Persons and the Covenant on Civil Freedoms, all of which bind the nations to their promises.</li>
    <li>That in this <span class="key-big">COMMON CHARTER OF PERSONS, ARTICLE 19,</span> paragraph three, the nations have explicitly recognised that no lawful purpose can justify the silencing of a free voice, and that speech is the first guard of all the Rights and Sovereignty of the Individual.</li>
    <li>That the gifted history of Mankind has shown that all Central Governing Bodies result in the Tyranny of the few over the many and that the fragility of Free and Open Societies are nowhere more exposed than when Science is Politicized, and that in the face of bad or misguided authorities the power of the Citizen is to refuse.</li>
    <li>That I do recognize that this movement and the sovereignty expressed here proclaim that I am not bound or represented by this organisation, and that the absence of an impartial and just legal course of protection against the Public Institutions of this world leaves the right of choice with the individual alone.</li>
    <li>And that in signing this document, I explicitly reject the idea that any nation, convention, international body or institution can be deemed or stand to be justified in a mandate for tyranny or decisions I have not consented to.</li>
    <li><span class="key-big">THEREFORE,</span> I, hereby state that I do not recognize or be represented by any unelected Global Public Governance or Institutions, its ideology and tenets and confirm that I am a Sovereign Human Being beholden to no one, except that as it lies among Equal Participants of Society, I bear certain unalienable Rights and Responsibilities that are consistent with the Principles of Free and Democratic Nations of Laws, based upon our Western Enlightened Values.</li>
    <li>And that I call upon my fellow kind, by signing this document, to join the Guild of Lucid Observant Wanderers and together develop the Citizen, Constitutional and Judicial collective for the common good, <span class="mark">the very guarantee of the shared and ultimate ideals of those noble values which we all are entitled to, recognised as one.</span></li>
  </ul>
</main>
</body>
</html>
```